Steady Ground for Your Venture - book cover

A book cover (front) to be used on print book. Book will be 5 inches by 8 inches. Also need the cover image (as jpg) for promotional purposes. Include company logo on cover - I've included a couple of versions. Include my name as author: Dr. Lorinda Haskell

Title of book is:
Weatherizing Your Enterprise
(sub-title) by teaching thinking skills

this can be a sub-sub title, or a call out or "burst" standing alone -
A survival guide for 21st century business

If you'd like some inspiration, check out my web page: www.lessonmedic.net
The company colors are red, white and blue, but I think red might be too harsh - use with caution if you use it.
RGB values of the company are:
Blue: 0/66/105
Red: 190/30/45

Target Market(s)

Business / Professionals / Chief Executives of Companies with more than 1000 employees

Industry/Entity Type

Business

Font styles to use
Serif

Colors
0255a3
ffffff

Requirements
Must have
• The title should make them pause and say "I need to get this book if I want my company to survive another 20 years!"
Nice to have
• Some image that signifies the future and / or uncertainty. Should be abstract - not people, not technology (which could change and then make the book look old). If you'd like to make the design a wrap from front to back, that is fine. I am not sure what text will go on the back at this point, so I may have to come back to you in a few months for an update.

```html
<!DOCTYPE html>
<html lang="en">
<head>
<meta charset="utf-8">
<title>Weatherizing Your Enterprise – Book Cover</title>
<link rel="stylesheet" href="https://fonts.googleapis.com/css2?family=Oswald:wght@600;700&family=Tinos:wght@400;700&display=swap">
<style>
  :root {
    --navy: #0a3a66;
    --title-blue: #0d3d68;
    --brand-red: #be1e2d;
    --white: #ffffff;
    --sky-top: #6f9fd0;
    --sky-mid: #d7e6f2;
    --sun: #f6e3a8;
    --sea: #6f8fae;
    --deep: #0b3664;
  }
  html, body {
    margin: 0;
    padding: 0;
    overflow: hidden;
    background: #e9eef3;
  }
  .cover {
    position: relative;
    width: 750px;
    height: 1200px;
    overflow: hidden;
    background: var(--deep);
  }
  .cover-scene {
    position: absolute;
    inset: 0;
    background:
      radial-gradient(ellipse 260px 160px at 250px 740px, rgba(255,244,205,0.95), rgba(246,227,168,0.55) 45%, rgba(246,227,168,0) 100%),
      linear-gradient(180deg,
        var(--sky-top) 0%,
        #a9c8e6 12%,
        var(--sky-mid) 28%,
        #eef3f6 44%,
        #cfdbe6 56%,
        #f0e6c8 62%,
        var(--sea) 70%,
        #4b6f95 78%,
        var(--deep) 88%,
        var(--navy) 100%);
  }
  .cover-scene .hourglass-zone {
    position: absolute;
    left: 430px;
    top: 400px;
    width: 290px;
    height: 560px;
    background: linear-gradient(180deg, rgba(40,55,75,0.35), rgba(230,236,240,0.25) 40%, rgba(40,55,75,0.4));
    border-radius: 12px;
  }
  .title {
    position: absolute;
    top: 8px;
    left: 0;
    width: 750px;
    margin: 0;
    text-align: center;
    font-family: "Oswald", sans-serif;
    font-weight: 700;
    font-size: 86px;
    line-height: 0.9;
    letter-spacing: -1px;
    color: var(--title-blue);
  }
  .subtitle {
    position: absolute;
    top: 248px;
    left: 0;
    width: 750px;
    margin: 0;
    text-align: center;
    font-family: "Tinos", serif;
    font-weight: 400;
    font-size: 50px;
    color: var(--brand-red);
  }
  .burst {
    position: absolute;
    left: 70px;
    top: 372px;
    width: 330px;
    height: 330px;
  }
  .burst-text {
    position: absolute;
    left: 70px;
    top: 440px;
    width: 330px;
    margin: 0;
    text-align: center;
    font-family: "Oswald", sans-serif;
    font-weight: 600;
    font-size: 44px;
    line-height: 1.08;
    color: var(--white);
  }
  .author {
    position: absolute;
    top: 948px;
    left: 0;
    width: 750px;
    margin: 0;
    text-align: center;
    font-family: "Tinos", serif;
    font-weight: 400;
    font-size: 54px;
    color: var(--white);
  }
  .publisher {
    position: absolute;
    top: 1082px;
    left: 0;
    width: 750px;
    display: flex;
    justify-content: center;
    align-items: center;
    gap: 12px;
    font-family: "Tinos", serif;
    font-weight: 700;
    font-size: 40px;
    color: var(--white);
  }
  .publisher-dot {
    width: 12px;
    height: 12px;
    border-radius: 50%;
    background: var(--white);
  }
</style>
</head>
<body>
  <main class="cover">
    <div class="cover-scene" role="img" aria-label="Photograph of a sunrise over the sea under a pale blue sky, with an antique hourglass standing on a rock at the right">
      <div class="hourglass-zone"></div>
    </div>

    <h1 class="title">Weatherizing<br>Your Enterprise</h1>
    <p class="subtitle">by teaching thinking skills</p>

    <svg class="burst" viewBox="0 0 330 330" aria-hidden="true">
      <circle cx="165" cy="165" r="163" fill="var(--brand-red)"/>
      <circle cx="165" cy="165" r="148" fill="none" stroke="var(--white)" stroke-width="1.5"/>
    </svg>
    <p class="burst-text">A Survival<br>Guide For<br>21st Century<br>Business</p>

    <p class="author">Dr. Lorinda Haskell</p>

    <div class="publisher">
      <span class="publisher-dot"></span>
      <span class="publisher-name">Lesson Medic</span>
    </div>
  </main>
</body>
</html>
```